Vesk Architecture

We are a architectural design and build company working between scales 1/1000 to 1/1 we want people to understand our difference from our design experience and quality.we build hotels restourants and office spaces.Our company name is Vesk architecture to mind sustainability.

We want to write our adress phone and work spesifications on the card and we want our logo as backround.

Ps:you could find the logo adress and phone box numbers from the web:www.veskmimarlik-ornek.com

Target Market(s)

Who looks for experts.

Industry/Entity Type

Architecture

Requirements
Must have
• Design is over everything.
Should not have
• we don want it to be colorfull

```html
<!DOCTYPE html>
<html lang="tr">
<head>
<meta charset="utf-8">
<title>Vesk Mimarlık – Kartvizit</title>
<link rel="stylesheet" href="https://fonts.googleapis.com/css2?family=Source+Sans+3:wght@300;400;600;700&display=swap">
<style>
  :root {
    --stage-teal: #1e5661;
    --stage-dark: #1a1a1a;
    --card-white: #ffffff;
    --pattern-grey: #e3e8eb;
    --brand-teal: #0f4a5a;
    --pattern-teal: #2b6474;
    --ink: #231f20;
    --ink-soft: #3a3a3a;
  }
  * { margin: 0; padding: 0; box-sizing: border-box; }
  html, body { width: 1198px; height: 1200px; overflow: hidden; }
  body {
    font-family: "Source Sans 3", "Segoe UI", sans-serif;
    background: linear-gradient(135deg, var(--stage-teal) 0%, #1b2e33 38%, var(--stage-dark) 62%, #161616 100%);
    position: relative;
  }
  .card {
    position: absolute;
    width: 795px;
    height: 485px;
    overflow: hidden;
  }
  .card--front {
    left: 90px; top: 90px;
    background: var(--card-white);
    border-radius: 64px 0 64px 0;
  }
  .card--back {
    left: 315px; top: 622px;
    background: var(--brand-teal);
    border-radius: 0 64px 0 64px;
  }
  .card__pattern {
    position: absolute; inset: 0;
  }
  .card--front .card__pattern {
    background: linear-gradient(160deg, var(--pattern-grey) 0%, #f1f3f5 45%, var(--card-white) 80%);
  }
  .card--back .card__pattern {
    background: linear-gradient(160deg, var(--pattern-teal) 0%, #1f5868 60%, var(--brand-teal) 100%);
  }
  .wordmark {
    position: absolute;
    display: flex;
    flex-direction: column;
    align-items: flex-end;
    line-height: 1;
  }
  .wordmark__name {
    font-weight: 300;
    letter-spacing: 2px;
  }
  .wordmark__sub {
    font-weight: 300;
    letter-spacing: 4px;
  }
  .card--front .wordmark {
    left: 60px; top: 40px;
    color: var(--ink);
    transform: rotate(-8deg);
    transform-origin: left bottom;
  }
  .card--front .wordmark__name { font-size: 132px; }
  .card--front .wordmark__sub { font-size: 26px; margin-top: -4px; margin-right: 78px; }
  .card--back .wordmark {
    left: 50%; top: 50%;
    transform: translate(-50%, -50%);
    color: var(--card-white);
  }
  .card--back .wordmark__name { font-size: 104px; }
  .card--back .wordmark__sub { font-size: 20px; margin-top: -2px; margin-right: 58px; }
  .contact {
    position: absolute;
    right: 30px; bottom: 72px;
    text-align: right;
    color: var(--ink-soft);
    font-size: 19px;
    line-height: 1.45;
    transform: rotate(-12deg);
    transform-origin: right bottom;
  }
  .contact__street {
    color: var(--brand-teal);
    font-weight: 700;
    font-size: 19px;
  }
  .contact__label {
    color: var(--brand-teal);
    font-weight: 700;
    margin-right: 8px;
  }
  .contact__line { display: block; }
</style>
</head>
<body>
  <article class="card card--front">
    <div class="card__pattern" role="img" aria-label="Açık gri tekrar eden marka deseni arka planı"></div>
    <div class="wordmark">
      <span class="wordmark__name">vesk</span>
      <span class="wordmark__sub">MİMARLIK</span>
    </div>
    <address class="contact" style="font-style: normal;">
      <span class="contact__line contact__street">Kuyubaşı Mah. Tekin Cad. Lale Sokl.</span>
      <span class="contact__line">No.7 Fenerbahçe Kadıköy/istanbul</span>
      <span class="contact__line"><span class="contact__label">t.</span>0216 555 01 47</span>
      <span class="contact__line"><span class="contact__label">f.</span>0216 555 01 48</span>
      <span class="contact__line"><span class="contact__label">e.</span>veskmimarlik@ornek-posta.com</span>
    </address>
  </article>

  <article class="card card--back">
    <div class="card__pattern" role="img" aria-label="Koyu petrol mavisi üzerinde tekrar eden marka deseni arka planı"></div>
    <div class="wordmark">
      <span class="wordmark__name">vesk</span>
      <span class="wordmark__sub">MİMARLIK</span>
    </div>
  </article>
</body>
</html>
```